Business card design for a dynamic IT consulting company

We need a business card design for a young firm, specialized in the Telecommunications/Consulting industry. The name of the company is Brask and Partners Business Consulting Ltd. (Short name: Brask and Partnes)
Brask = solve read reverse, so we aim to be uncomplicated and solution-oriented. The small pipe in our logo is also related to the word solve. So we need a new business card design, which is simple, eye catching and something non traditional (I would probably prefer a square shaped design rather than a rectangle, but open for suggestions). Attached our logo.

Target Market(s)

Usually our customers are Tier1 Telecoms providers (Q-Linkra, Parnexo, etc) and their executives.

Industry/Entity Type

Business

Contact Information for Business Card

Name: Gergely Halmindo
Email: g.halmindo@braskpartnera.hu
Web: www.braskpartnera.hu
Mobile: +36 30 555 0192
Title: Managing Director

Optional:
Company name: Brask and Partners Ltd.
Address: 1047 Budapest, Ravaszi str. 17/B, Hungary

Font styles to use
Other font styles liked:
• helveticaneue_medium, Prime Regular are used now.

Colors

Designer to choose colors to be used in the design.

Requirements
Must have
• I would like to have a 2 sided design.
Nice to have
• I thought if we make the logo a bit bigger (without the company name), that could go to the back with the company name below. I though, if the pipe in the logo is somehow touchable on the business card, would be nice and unique.

```html
<!DOCTYPE html>
<html lang="en">
<head>
<meta charset="utf-8">
<title>Brask and Partners – Business Card</title>
<link rel="stylesheet" href="https://fonts.googleapis.com/css2?family=Archivo:wght@800&family=Roboto+Condensed:wght@300;400&display=swap">
<style>
  :root {
    --page: #ffffff;
    --card: #363435;
    --ink: #ffffff;
    --accent-blue: #0a96d6;
    --accent-magenta: #b3338a;
    --body-font: "Roboto Condensed", "Arial Narrow", sans-serif;
    --name-font: "Archivo", "Arial Black", sans-serif;
  }
  * { margin: 0; padding: 0; box-sizing: border-box; }
  html, body {
    width: 1200px; height: 1000px; overflow: hidden;
    background: var(--page);
  }
  .sheet { position: relative; width: 1200px; height: 1000px; }
  .card {
    position: absolute; left: 209px; width: 781px; height: 447px;
    background: var(--card); color: var(--ink);
    font-family: var(--body-font);
  }
  .card--front { top: 31px; }
  .card--back { top: 521px; }

  .wordmark {
    position: absolute; display: flex; align-items: center; gap: 14px;
    font-family: var(--body-font); font-weight: 300;
    color: var(--ink); white-space: nowrap; line-height: 1;
  }
  .wordmark__square {
    display: block; width: 18px; height: 18px;
    background: var(--accent-magenta);
  }
  .card--front .wordmark { right: 30px; top: 28px; font-size: 50px; }
  .card--back .wordmark {
    left: 50%; transform: translateX(-50%); top: 318px; font-size: 52px;
  }

  .contact { position: absolute; left: 39px; top: 240px; }
  .contact__name {
    font-family: var(--name-font); font-weight: 800;
    font-size: 21px; letter-spacing: 0.3px;
    color: var(--accent-blue); line-height: 1;
  }
  .contact__title { font-size: 19px; margin-top: 8px; line-height: 1; }
  .contact__list { list-style: none; margin-top: 22px; }
  .contact__item {
    display: flex; align-items: center; gap: 10px;
    font-size: 19px; line-height: 1; height: 24px;
  }
  .contact__item + .contact__item { margin-top: 1px; }
  .contact__icon { width: 16px; height: 16px; flex: none; }
  .contact__address { font-size: 19px; margin-top: 9px; line-height: 1; }

  .company-name {
    position: absolute; left: 0; right: 0; top: 402px;
    text-align: center; font-size: 20px; line-height: 1;
  }
</style>
</head>
<body>
<main class="sheet">
  <section class="card card--front" aria-label="Business card front">
    <div class="wordmark"><span class="wordmark__square"></span>Brask &amp; Partners</div>

    <div class="contact">
      <h1 class="contact__name">Gergely Halmindo</h1>
      <p class="contact__title">Managing Director</p>
      <ul class="contact__list">
        <li class="contact__item">
          <svg class="contact__icon" viewBox="0 0 16 16" aria-hidden="true">
            <rect width="16" height="16" rx="3" fill="#fff"/>
            <path d="M5.5 3.5c-1.5 1-1.8 3-.8 5s2.8 3.8 4.6 4.2c1 .2 1.6-.2 2-.8l-1.5-1.5c-.4.4-.9.5-1.4.1-.8-.7-1.6-1.6-2-2.5-.2-.5 0-.9.4-1.2L5.5 3.5z" fill="#363435"/>
          </svg>
          +36 30 555 0192
        </li>
        <li class="contact__item">
          <svg class="contact__icon" viewBox="0 0 16 16" aria-hidden="true">
            <rect width="16" height="16" rx="3" fill="#fff"/>
            <rect x="3" y="5" width="10" height="7" fill="none" stroke="#363435" stroke-width="1.4"/>
            <path d="M3 5l5 4 5-4" fill="none" stroke="#363435" stroke-width="1.4"/>
          </svg>
          g.halmindo@braskpartnera.hu
        </li>
        <li class="contact__item">
          <svg class="contact__icon" viewBox="0 0 16 16" aria-hidden="true">
            <rect width="16" height="16" rx="3" fill="#fff"/>
            <circle cx="8" cy="8" r="4.8" fill="none" stroke="#363435" stroke-width="1.2"/>
            <ellipse cx="8" cy="8" rx="2" ry="4.8" fill="none" stroke="#363435" stroke-width="1"/>
            <path d="M3.2 8h9.6" stroke="#363435" stroke-width="1"/>
          </svg>
          www.braskpartnera.hu
        </li>
      </ul>
      <p class="contact__address">1047 Budapest, Ravaszi str. 17/B, Hungary</p>
    </div>
  </section>

  <section class="card card--back" aria-label="Business card back">
    <div class="wordmark"><span class="wordmark__square"></span>Brask &amp; Partners</div>
    <p class="company-name">Brask and Partners Ltd.</p>
  </section>
</main>
</body>
</html>
```